Print on top the name of the company: (Or Similar)
Bellhaven Cleaning & Disinfecting
Because your standards aren't standard.

We adhere to ALL FHB guidelines for both residential and commercial cleaning.

Infection Control is our ultimate goal.

Instructions:
Opening a residential and commercial cleaning and disinfecting company in south Florida.

Targeting high-end residential clients, commercial and healthcare facilities, specializing in Ambulatory Care Guidelines. With a concentration and expertise in targeting Covid 19 and other transmissible pathogens.

TWLR trained.
Owned and operated by a licensed BSN Registered Nurse specially ​trained in Infection Control Prevention with over 25 years experience. Over two decades in Ambulatory Surgery Center Administration, Director of Nursing and Infection Control Prevention ad Consulting.

Looking to create a business flier that emphasizes Cleaning & Disinfection
along with the standard expectation for residential and Commercial cleaning services

Target Market(s)

Residential & Commercial

Font styles to use
Decorative

Requirements
Must have
• A checklist for cleaning services

```html
<!DOCTYPE html>
<html lang="en">
<head>
<meta charset="utf-8">
<title>Bellhaven Cleaning &amp; Disinfecting – Flyer</title>
<link href="https://fonts.googleapis.com/css2?family=Lato:wght@400;700;900&display=swap" rel="stylesheet">
<style>
  :root {
    --blue: #0a5fc4;
    --orange: #f39200;
    --ink: #151515;
    --white: #ffffff;
    --page: #e4e4e4;
    --hero-top: #f4f7fb;
    --hero-bottom: #e3ebf4;
  }
  * { box-sizing: border-box; margin: 0; padding: 0; }
  html, body { width: 990px; height: 1200px; overflow: hidden; background: var(--page); }
  body { position: relative; font-family: "Lato", sans-serif; }

  .flyer {
    position: absolute; left: 31.5px; top: 0;
    width: 1188px; height: 1538px;
    transform: scale(0.7802); transform-origin: top left;
    background: var(--white); overflow: hidden;
  }
  .abs { position: absolute; white-space: nowrap; }

  /* hero */
  .hero { left: 0; top: 0; width: 1188px; height: 728px;
    background: linear-gradient(180deg, var(--hero-top), var(--hero-bottom)); }
  .hero-photo { left: 600px; top: 0; width: 588px; height: 728px;
    background: radial-gradient(ellipse at 55% 45%, #ffffff 0%, #eef2f7 45%, #c9d7e6 100%); }
  .brand { left: 88px; top: 62px; font-size: 106px; font-weight: 900; color: var(--blue); letter-spacing: -1px; line-height: 1.1; }
  .brand-bar { left: 91px; top: 177px; width: 577px; height: 61px; background: var(--orange);
    color: var(--white); font-size: 40px; font-weight: 900; line-height: 61px; text-align: center; }
  .tagline { left: 90px; top: 260px; font-size: 52px; font-weight: 700; color: var(--ink); line-height: 1.25; }
  .specialty { left: 91px; top: 439px; width: 470px; height: 68px; border: 2px solid var(--orange); }
  .specialty-text { left: 118px; top: 416px; font-size: 32px; font-weight: 900; color: var(--blue); line-height: 38px; }
  .specialty-text span { background: #eaf0f6; padding: 0 8px 0 6px; }
  .specialty-text .second { background: none; padding-left: 6px; }
  .guidelines { left: 91px; top: 548px; font-size: 29px; font-weight: 700; color: var(--ink); line-height: 36px; }
  .goal { left: 91px; top: 637px; width: 572px; height: 46px; }
  .goal-text { left: 123px; top: 637px; font-size: 29px; color: var(--white); line-height: 46px; font-weight: 700; }

  /* services */
  .services { left: 0; top: 728px; width: 1188px; height: 444px; background: var(--orange); }
  .services-tab { left: 0; top: 728px; width: 1188px; height: 80px; }
  .services-title { left: 74px; top: 737px; font-size: 52px; font-weight: 900; color: var(--white); line-height: 64px; }
  .col-head { font-size: 32px; font-weight: 900; color: var(--white); top: 826px; }
  .col-rule { top: 870px; height: 3px; width: 305px; background: var(--white); }
  .checklist { list-style: none; top: 888px; }
  .checklist li { display: flex; align-items: center; gap: 10px; height: 32.5px;
    font-size: 24px; font-weight: 700; color: var(--white); }
  .checklist svg { width: 22px; height: 22px; flex: none; }
  .photo { width: 306px; height: 188px; }
  .photo::after { content: ""; position: absolute; left: 8px; top: 8px; right: 8px; bottom: 8px; border: 2px solid rgba(255,255,255,.85); }
  .photo-office { left: 808px; top: 762px; background: linear-gradient(135deg, #7fa8b8, #2f4a66 60%, #d9dde2); }
  .photo-mop { left: 808px; top: 974px; background: linear-gradient(180deg, #e8e4dc, #c9c4bb 55%, #e8733a 80%, #d9d6d0); }

  /* credentials */
  .badge { left: 77px; top: 1222px; width: 156px; height: 136px; border-radius: 50%; background: #d4202a; border: 7px solid var(--ink); }
  .divider { left: 253px; top: 1205px; width: 2px; height: 170px; background: var(--orange); }
  .trained-tab { left: 273px; top: 1213px; width: 232px; height: 32px; }
  .trained-text { left: 293px; top: 1213px; font-size: 24px; font-weight: 900; color: var(--white); line-height: 32px; }
  .bio { left: 273px; top: 1251px; font-size: 19px; line-height: 23.5px; color: var(--ink); }
  .photo-crew { left: 808px; top: 1187px; background: linear-gradient(135deg, #dfe4e8, #9aa8b2 50%, #f2f4f5); }
  .region { left: 0; top: 1400px; width: 1188px; text-align: center; font-size: 29.5px; font-weight: 900; color: var(--blue); }

  /* contact */
  .contact-band { left: 0; top: 1478px; width: 1188px; height: 60px; background: var(--blue); }
  .contact-pill { left: 90px; top: 1448px; width: 1024px; height: 57px; border-radius: 28px; background: var(--white); }
  .phone-icon { left: 72px; top: 1446px; width: 60px; height: 60px; }
  .quote { left: 143px; top: 1448px; font-size: 35px; font-weight: 900; color: var(--orange); line-height: 57px; }
  .mail-icon { left: 788px; top: 1452px; width: 50px; height: 50px; }
  .email { left: 850px; top: 1448px; font-size: 28px; font-weight: 700; color: var(--ink); line-height: 57px; }
</style>
</head>
<body>
<main class="flyer">
  <div class="abs hero"></div>
  <div class="abs hero-photo" role="img" aria-label="Technician in white protective suit, goggles and mask holding a disinfectant sprayer"></div>

  <h1 class="abs brand">BELLHAVEN</h1>
  <div class="abs brand-bar">CLEANING &amp; DISINFECTING</div>
  <p class="abs tagline">Because your standards<br>aren't standard.</p>

  <div class="abs specialty"></div>
  <p class="abs specialty-text"><span>Specializing In</span><br><span class="second">Ambulatory Care Guidelines.</span></p>

  <p class="abs guidelines">We adhere to ALL FHB guidelines for both<br>residential and commercial cleaning.</p>
  <svg class="abs goal" viewBox="0 0 572 46"><polygon points="0,0 545,0 572,46 0,46" fill="var(--blue)"/></svg>
  <p class="abs goal-text">Infection Control is our ultimate goal.</p>

  <section>
    <div class="abs services"></div>
    <svg class="abs services-tab" viewBox="0 0 1188 80">
      <rect x="0" y="0" width="1188" height="5" fill="var(--blue)"/>
      <polygon points="0,0 724,0 672,80 0,80" fill="var(--blue)"/>
    </svg>
    <h2 class="abs services-title">WE ARE EXPERT IN</h2>

    <h3 class="abs col-head" style="left:74px">COMMERCIAL</h3>
    <div class="abs col-rule" style="left:74px"></div>
    <ul class="abs checklist" style="left:74px">
      <li><svg viewBox="0 0 22 22"><circle cx="11" cy="11" r="9.5" fill="none" stroke="#fff" stroke-width="1.6"/><path d="M6.5 11.3l3 3 6-6" fill="none" stroke="#fff" stroke-width="1.8"/></svg>Janitorial</li>
      <li><svg viewBox="0 0 22 22"><circle cx="11" cy="11" r="9.5" fill="none" stroke="#fff" stroke-width="1.6"/><path d="M6.5 11.3l3 3 6-6" fill="none" stroke="#fff" stroke-width="1.8"/></svg>Offices</li>
      <li><svg viewBox="0 0 22 22"><circle cx="11" cy="11" r="9.5" fill="none" stroke="#fff" stroke-width="1.6"/><path d="M6.5 11.3l3 3 6-6" fill="none" stroke="#fff" stroke-width="1.8"/></svg>Floor Maintenance</li>
      <li><svg viewBox="0 0 22 22"><circle cx="11" cy="11" r="9.5" fill="none" stroke="#fff" stroke-width="1.6"/><path d="M6.5 11.3l3 3 6-6" fill="none" stroke="#fff" stroke-width="1.8"/></svg>Carpet cleaning</li>
      <li><svg viewBox="0 0 22 22"><circle cx="11" cy="11" r="9.5" fill="none" stroke="#fff" stroke-width="1.6"/><path d="M6.5 11.3l3 3 6-6" fill="none" stroke="#fff" stroke-width="1.8"/></svg>Move-ins</li>
      <li><svg viewBox="0 0 22 22"><circle cx="11" cy="11" r="9.5" fill="none" stroke="#fff" stroke-width="1.6"/><path d="M6.5 11.3l3 3 6-6" fill="none" stroke="#fff" stroke-width="1.8"/></svg>Move-outs</li>
      <li><svg viewBox="0 0 22 22"><circle cx="11" cy="11" r="9.5" fill="none" stroke="#fff" stroke-width="1.6"/><path d="M6.5 11.3l3 3 6-6" fill="none" stroke="#fff" stroke-width="1.8"/></svg>Constructions clean-ups</li>
      <li><svg viewBox="0 0 22 22"><circle cx="11" cy="11" r="9.5" fill="none" stroke="#fff" stroke-width="1.6"/><path d="M6.5 11.3l3 3 6-6" fill="none" stroke="#fff" stroke-width="1.8"/></svg>Estate clean-outs</li>
    </ul>

    <h3 class="abs col-head" style="left:418px">RESIDENTIAL</h3>
    <div class="abs col-rule" style="left:420px"></div>
    <ul class="abs checklist" style="left:420px">
      <li><svg viewBox="0 0 22 22"><circle cx="11" cy="11" r="9.5" fill="none" stroke="#fff" stroke-width="1.6"/><path d="M6.5 11.3l3 3 6-6" fill="none" stroke="#fff" stroke-width="1.8"/></svg>House Cleaning</li>
      <li><svg viewBox="0 0 22 22"><circle cx="11" cy="11" r="9.5" fill="none" stroke="#fff" stroke-width="1.6"/><path d="M6.5 11.3l3 3 6-6" fill="none" stroke="#fff" stroke-width="1.8"/></svg>before and After party</li>
      <li><svg viewBox="0 0 22 22"><circle cx="11" cy="11" r="9.5" fill="none" stroke="#fff" stroke-width="1.6"/><path d="M6.5 11.3l3 3 6-6" fill="none" stroke="#fff" stroke-width="1.8"/></svg>Move-ins</li>
      <li><svg viewBox="0 0 22 22"><circle cx="11" cy="11" r="9.5" fill="none" stroke="#fff" stroke-width="1.6"/><path d="M6.5 11.3l3 3 6-6" fill="none" stroke="#fff" stroke-width="1.8"/></svg>Move-outs</li>
      <li><svg viewBox="0 0 22 22"><circle cx="11" cy="11" r="9.5" fill="none" stroke="#fff" stroke-width="1.6"/><path d="M6.5 11.3l3 3 6-6" fill="none" stroke="#fff" stroke-width="1.8"/></svg>Holiday Cleaning</li>
      <li><svg viewBox="0 0 22 22"><circle cx="11" cy="11" r="9.5" fill="none" stroke="#fff" stroke-width="1.6"/><path d="M6.5 11.3l3 3 6-6" fill="none" stroke="#fff" stroke-width="1.8"/></svg>Seasonal Cleaning</li>
      <li><svg viewBox="0 0 22 22"><circle cx="11" cy="11" r="9.5" fill="none" stroke="#fff" stroke-width="1.6"/><path d="M6.5 11.3l3 3 6-6" fill="none" stroke="#fff" stroke-width="1.8"/></svg>Carpet Cleaning</li>
      <li><svg viewBox="0 0 22 22"><circle cx="11" cy="11" r="9.5" fill="none" stroke="#fff" stroke-width="1.6"/><path d="M6.5 11.3l3 3 6-6" fill="none" stroke="#fff" stroke-width="1.8"/></svg>Deodorizing and Sanitizing</li>
    </ul>

    <div class="abs photo photo-office" role="img" aria-label="Cleaning crew in aprons and yellow gloves cleaning an office"></div>
    <div class="abs photo photo-mop" role="img" aria-label="Flat mop and orange bucket on a clean floor"></div>
  </section>

  <section>
    <div class="abs badge" role="img" aria-label="Certification badge"></div>
    <div class="abs divider"></div>
    <svg class="abs trained-tab" viewBox="0 0 232 32"><polygon points="0,0 212,0 232,32 0,32" fill="var(--blue)"/></svg>
    <p class="abs trained-text">TWLR Trained</p>
    <p class="abs bio">Owned and operated by a licensed BSN Registered<br>Nurse specially trained in Infection Control Prevention with<br>over 25 years experience. Over two decades in Ambulatory<br>Surgery Center Administration, Director of Nursing and<br>Infection Control Prevention ad Consulting.</p>
    <div class="abs photo photo-crew" role="img" aria-label="Technicians in protective suits disinfecting an office"></div>
    <p class="abs region">Residential And Commercial Cleaning And Disinfecting Company In South Florida</p>
  </section>

  <footer>
    <div class="abs contact-band"></div>
    <div class="abs contact-pill"></div>
    <svg class="abs phone-icon" viewBox="0 0 60 60">
      <circle cx="30" cy="30" r="28" fill="var(--blue)" stroke="#fff" stroke-width="3"/>
      <path d="M21 16c2-1 4 0 5 2l2 5c1 2 0 3-1 4l-2 2c1 4 4 7 8 9l2-2c1-1 2-2 4-1l5 2c2 1 3 3 2 5l-1 2c-1 2-3 3-6 2-10-3-17-10-20-20-1-3 0-6 2-7z" fill="#fff"/>
    </svg>
    <p class="abs quote">CALL FOR FREE QUOTE: 0123 456 789</p>
    <svg class="abs mail-icon" viewBox="0 0 50 50">
      <circle cx="25" cy="25" r="22" fill="#fff" stroke="var(--blue)" stroke-width="2.5"/>
      <rect x="14" y="17" width="22" height="16" rx="1.5" fill="none" stroke="var(--blue)" stroke-width="2"/>
      <path d="M14 18l11 9 11-9" fill="none" stroke="var(--blue)" stroke-width="2"/>
    </svg>
    <p class="abs email">info@yourmail.com</p>
  </footer>
</main>
</body>
</html>
```